Pet and Potrait photography business needs web site design

I need a web design that is for a portrait and pet photography business based in Tasmania, Australia. It is a small, simple concept, photography business that focuses on portraits and pet photography only. I need something that is clean, maybe a white background, fun, and appealing to families. The design must make my images stand out and be the focus. The final design needs to show that it is aimed a families, pet owners, and is all about the clients - albeit the two or four legged kinds.

Business name is: reed and willow photography

I need it to be able to have the following:

- Include space for logo design which is also through SketchHarbor
- Home Page which has a gallery of my images (which you can click an arrow - either forward or back - that showcases my images
- About Page
- Portfolio Page (preferably two a) for portraits, and b) for pet photography
- Pricing page
- secure log in client page
- Contact page

Reason: Waiting for logo design to be completed to fit in with overall website design.

Target Market(s)

Families
Pet owners
Single couples who have fur babies

Industry/Entity Type

Business

Font styles to use
Serif
Decorative
Script

Colors

Designer to choose colors to be used in the design.

Requirements
Must have
• the website must provide the ability for me to upload and change images regularly.
Nice to have
• Logo design is a secondary project that will need to be worked on as well. I will pay an additional amount for those that are prepared to include this in the project.
Should not have
• No graffiti style writing.
It has to be elegant, and stylish and be aimed at females.
Women are going to be the driver for having portraits done of either their babies, children, or fur babies - i.e. pets.

```html
<!DOCTYPE html>
<html lang="en">
<head>
<meta charset="utf-8">
<title>Reed &amp; Willow Photography</title>
<link rel="stylesheet" href="https://fonts.googleapis.com/css2?family=Oswald:wght@400;500&family=Kaushan+Script&family=Delius&family=Playball&display=swap">
<style>
  :root {
    --page: #f1f1f1;
    --hero-top: #e4efe9;
    --hero-bottom: #dcebe5;
    --teal-dark: #0f3434;
    --heading: #1c3434;
    --accent-red: #b51d2c;
    --link-blue: #2a8fd0;
    --text: #333333;
    --muted: #555555;
    --panel: #e6f2f1;
    --hex-bg: #cde8ea;
    --rule: #d8d8d8;
    --white: #ffffff;
  }
  * { box-sizing: border-box; margin: 0; padding: 0; }
  html, body { width: 1054px; height: 1200px; overflow: hidden; background: var(--page); }
  body { font-family: Arial, Helvetica, sans-serif; color: var(--text); }
  .canvas { position: relative; width: 1054px; height: 1200px; overflow: hidden; background: var(--page); }

  .hero-backdrop {
    position: absolute; left: 0; top: 0; width: 1054px; height: 522px;
    background: linear-gradient(180deg, var(--hero-top) 0%, #eef4f0 55%, var(--hero-bottom) 100%);
  }

  .account-links { position: absolute; left: 120px; top: 22px; display: flex; gap: 14px; font-size: 12px; }
  .account-links a { color: var(--accent-red); text-decoration: none; }

  .brand {
    position: absolute; left: 425px; top: 24px; width: 200px; height: 92px;
    display: flex; align-items: center; justify-content: center; text-align: center;
    font-family: "Oswald", sans-serif; font-weight: 500; font-size: 19px; line-height: 1.2;
    color: var(--teal-dark);
  }

  .main-nav {
    position: absolute; left: 120px; top: 104px; width: 814px; height: 39px;
    background: var(--teal-dark); border-radius: 3px 3px 0 0;
  }
  .main-nav a {
    position: absolute; top: 0; height: 39px; line-height: 39px;
    color: var(--white); font-weight: bold; font-size: 14px; text-decoration: none;
  }
  .main-nav .is-active {
    top: 9px; height: 30px; line-height: 30px; left: 17px; width: 65px; text-align: center;
    background: var(--white); color: var(--teal-dark); border-radius: 3px 3px 0 0;
  }
  .main-nav .is-active::after {
    content: ""; position: absolute; left: 16px; right: 16px; bottom: 3px; height: 2px; background: var(--teal-dark);
  }
  .nav-divider { position: absolute; top: 10px; width: 1px; height: 20px; background: #2e5555; }

  .hero-photos { position: absolute; left: 120px; top: 150px; }
  .hero-glow {
    position: absolute; left: 640px; top: 150px; width: 290px; height: 240px;
    background: radial-gradient(ellipse at center, #e9d8c6 0%, rgba(240,232,222,0.7) 45%, rgba(238,244,240,0) 72%);
  }
  .hero-slogan {
    position: absolute; left: 554px; top: 322px; width: 284px; height: 146px;
    background: linear-gradient(135deg, #d7d2cd 0%, #c9a2a2 50%, #cfcbc7 100%);
    border-radius: 6px; opacity: 0.85;
  }

  .section-title {
    position: absolute; font-family: "Oswald", sans-serif; font-weight: 400; color: var(--heading);
  }
  .gallery-title { left: 120px; top: 540px; font-size: 29px; }
  .gallery-link {
    position: absolute; left: 864px; top: 573px; font-size: 10px; color: var(--text); text-decoration: underline;
  }
  .gallery-panel {
    position: absolute; left: 118px; top: 604px; width: 816px; height: 168px;
    background: var(--panel); border-radius: 8px; box-shadow: 0 6px 10px rgba(0,0,0,0.12);
  }
  .gallery-arrow { position: absolute; top: 668px; }
  .gallery-thumb { position: absolute; top: 624px; width: 122px; height: 122px; }
  .thumb-overlay { position: absolute; inset: 0; background: rgba(40,20,20,0.55); }
  .thumb-zoom { position: absolute; left: 35px; top: 38px; }

  .welcome-title {
    position: absolute; left: 120px; top: 812px; font-family: "Kaushan Script", cursive;
    font-size: 46px; color: var(--accent-red);
  }
  .welcome-rule { position: absolute; left: 120px; top: 876px; width: 302px; height: 1px; background: var(--rule); }
  .profile-frame {
    position: absolute; left: 120px; top: 900px; width: 116px; height: 116px;
    background: #cccccc; padding: 6px;
  }
  .profile-photo { width: 104px; height: 104px; background: linear-gradient(160deg, #d8b39a 0%, #c08f74 60%, #9a7460 100%); }
  .profile-caption {
    position: absolute; left: 256px; top: 938px; width: 160px;
    font-family: "Playball", cursive; font-size: 12px; line-height: 18px; color: var(--text);
  }
  .welcome-text {
    position: absolute; left: 122px; top: 1032px; width: 302px; font-size: 11px; line-height: 14px; color: var(--text);
  }
  .read-more {
    position: absolute; left: 354px; top: 1107px; font-size: 11px; color: var(--link-blue); text-decoration: underline;
  }

  .testimonials-title { left: 504px; top: 826px; font-size: 31px; font-weight: 500; }
  .testimonial-nav { position: absolute; left: 897px; top: 837px; display: flex; gap: 2px; }
  .testimonial-nav span { width: 17px; height: 17px; display: block; }
  .testimonial-nav .prev { background: #dcdcdc; }
  .testimonial-nav .next { background: var(--teal-dark); }
  .testimonial-quote {
    position: absolute; left: 492px; top: 904px; width: 276px; text-align: center;
    font-family: "Delius", cursive; font-size: 10.5px; line-height: 15px; color: var(--muted);
  }
  .testimonial-author {
    position: absolute; left: 492px; top: 985px; width: 276px; text-align: center;
    font-family: "Delius", cursive; font-size: 10.5px; color: var(--muted);
  }
  .testimonial-photo {
    position: absolute; left: 808px; top: 876px; width: 126px; height: 154px;
    background: linear-gradient(120deg, #c98e6e 0%, #e7c2a6 45%, #f1dccb 75%, #d9b89e 100%);
  }

  .footer-rule { position: absolute; left: 0; top: 1156px; width: 1054px; height: 1px; background: var(--rule); }
  .copyright { position: absolute; left: 120px; top: 1170px; font-size: 12.5px; color: var(--text); }
  .social-links { position: absolute; left: 800px; top: 1164px; display: flex; gap: 7px; }
  .social-links span { width: 28px; height: 30px; display: block; }
  .social-a { background: #2d5ea8; }
  .social-b { background: #35a9e0; }
  .social-c { background: #4a4a4a; }
  .social-d { background: #efa21f; }
</style>
</head>
<body>
<div class="canvas">
  <div class="hero-backdrop" role="img" aria-label="Soft mint background pattern"></div>

  <nav class="account-links">
    <a href="#">Register</a><a href="#">Log in</a><a href="#">Wishlist</a>
  </nav>

  <div class="brand">Reed &amp; Willow<br>Photography</div>

  <nav class="main-nav">
    <a class="is-active" href="#">Home</a>
    <a href="#" style="left:97px">Portfolio</a>
    <span class="nav-divider" style="left:166px"></span>
    <a href="#" style="left:184px">Pricing</a>
    <span class="nav-divider" style="left:245px"></span>
    <a href="#" style="left:263px">Services</a>
    <a href="#" style="left:502px">Contact Us</a>
  </nav>

  <svg class="hero-photos" width="420" height="360" viewBox="0 0 420 360">
    <g fill="var(--hex-bg)" opacity="0.8" stroke="var(--hex-bg)" stroke-width="14" stroke-linejoin="round">
      <polygon points="150,120 200,30 300,30 350,120 300,210 200,210"/>
      <polygon points="60,200 105,125 195,125 240,200 195,275 105,275"/>
    </g>
    <g stroke-linejoin="round" stroke-width="16">
      <polygon role="img" aria-label="Portrait photo of a smiling young girl" fill="#d9a98a" stroke="#d9a98a"
               points="18,124 60,48 146,48 188,124 146,200 60,200"/>
      <polygon role="img" aria-label="Portrait photo of a laughing girl" fill="#e0b394" stroke="#e0b394"
               points="216,84 248,26 318,26 350,84 318,142 248,142"/>
      <polygon role="img" aria-label="Photo of a tabby kitten among flowers" fill="#8d7d6e" stroke="#8d7d6e"
               points="180,266 216,200 290,200 326,266 290,332 216,332"/>
    </g>
    <g fill="#6b4a3a">
      <circle cx="103" cy="36" r="3"/><circle cx="283" cy="14" r="3"/><circle cx="253" cy="188" r="3"/>
    </g>
  </svg>

  <div class="hero-glow" role="img" aria-label="Faded portrait of a curly haired girl"></div>
  <div class="hero-slogan" role="img" aria-label="Hand lettered slogan: Everyone smiles in the same language"></div>

  <h2 class="section-title gallery-title">Image Gallery</h2>
  <a class="gallery-link" href="#">VISIT GALLERY</a>

  <div class="gallery-panel" role="img" aria-label="Soft mint patterned gallery strip"></div>
  <svg class="gallery-arrow" style="left:134px" width="25" height="25" viewBox="0 0 25 25" aria-label="Previous image">
    <circle cx="12.5" cy="12.5" r="12.5" fill="var(--teal-dark)"/>
    <polyline points="14.5,7.5 9.5,12.5 14.5,17.5" fill="none" stroke="#fff" stroke-width="2.5" stroke-linecap="round" stroke-linejoin="round"/>
  </svg>
  <svg class="gallery-arrow" style="left:894px" width="25" height="25" viewBox="0 0 25 25" aria-label="Next image">
    <circle cx="12.5" cy="12.5" r="12.5" fill="var(--teal-dark)"/>
    <polyline points="10.5,7.5 15.5,12.5 10.5,17.5" fill="none" stroke="#fff" stroke-width="2.5" stroke-linecap="round" stroke-linejoin="round"/>
  </svg>

  <div class="gallery-thumb" style="left:178px;background:linear-gradient(150deg,#b58a72,#7a5546)" role="img" aria-label="Photo of a child hugging">
    <div class="thumb-overlay"></div>
    <svg class="thumb-zoom" width="50" height="50" viewBox="0 0 50 50" aria-label="Enlarge image">
      <circle cx="25" cy="25" r="24" fill="#b0141f"/>
      <circle cx="27" cy="22" r="7" fill="none" stroke="#fff" stroke-width="3"/>
      <line x1="22" y1="27" x2="15" y2="34" stroke="#fff" stroke-width="4" stroke-linecap="round"/>
    </svg>
  </div>
  <div class="gallery-thumb" style="left:322px;background:linear-gradient(160deg,#4f9a3c,#2d6a2a 60%,#5a5a50)" role="img" aria-label="Photo of two green parrots"></div>
  <div class="gallery-thumb" style="left:467px;background:linear-gradient(160deg,#c8a070,#d9b59a 50%,#3d4a6a)" role="img" aria-label="Portrait photo of a smiling girl"></div>
  <div class="gallery-thumb" style="left:611px;background:linear-gradient(160deg,#d8c7b0,#6a6a5e 55%,#b8a48a)" role="img" aria-label="Photo of a baby turtle"></div>
  <div class="gallery-thumb" style="left:756px;background:linear-gradient(160deg,#d6b89a,#e8cdb4 50%,#9a8a6a)" role="img" aria-label="Portrait photo of a giggling girl"></div>

  <h2 class="welcome-title">Hi there!</h2>
  <div class="welcome-rule"></div>
  <div class="profile-frame"><div class="profile-photo" role="img" aria-label="Photographer portrait"></div></div>
  <p class="profile-caption">i am Lorem Ipsum, Proin gravida nibh vel velit auctor</p>
  <p class="welcome-text">Lorem Ipsum. Proin&nbsp; gravida nibh vel velit auctor aliquet. Aenean sollicitudin, lorem quis bibendum auctor, nisi elit consequat ipsum, nec sagittis sem nibh id elit. Duis llsed odio sit amet nibh vulputate cursus a sit amet maklkuris. Morbi accumsan ipsum velit.</p>
  <a class="read-more" href="#">Read More</a>

  <h2 class="section-title testimonials-title">Testimonials</h2>
  <div class="testimonial-nav"><span class="prev"></span><span class="next"></span></div>
  <p class="testimonial-quote">"Proin gravida nibh vel velit auctor aliquet. Aenean sollicitudin, lorem quis bibendum auctor, nisi elit consequat ipsum, nec sagittis sem nibh id elit. Duis sed odio sit amet nibh vulputate a sit amet mauris......"</p>
  <p class="testimonial-author">Owen MarshCEO, Company LTD</p>
  <div class="testimonial-photo" role="img" aria-label="Photo of a mother and baby smiling together"></div>

  <div class="footer-rule"></div>
  <p class="copyright">Copyright &reg; 2013 Reed and Willow Photography. All rights reserved</p>
  <div class="social-links">
    <span class="social-a" role="img" aria-label="Social link"></span>
    <span class="social-b" role="img" aria-label="Social link"></span>
    <span class="social-c" role="img" aria-label="Social link"></span>
    <span class="social-d" role="img" aria-label="News feed link"></span>
  </div>
</div>
</body>
</html>
```